Steadfast Voyage Partners Capability Statement

Steadfast Voyage Partners is a Corporate Travel Management company based in Brisbane, Australia. Please review our 'About Us' page of our website to gain an understanding of our company culture (www.steadfastvoyagepartners.example.com.au). We are extremely customer focused. We see ourselves as an extension of our client's business.We require a powerful 1 page infographic that highlights what we do - 'Capability Statement' to use as an initial introduction to prospect clients when they ask for information about us.* Our Core Competencies - Service / People / Technology (this is our tagline so I think the document should follow this format)* A Company snapshot - Office location and website (needs to be editable to add Licence information)* Performance / Key Benefits (needs to editable to add in testimonials and case studies)* Client retention result 96%* Employee retention 98%* Affiliations & Partnerships (we will add)*Awards (see details to include)* Contact Details (at the bottom of the page - Marcus Van Heerden marcus@svpartners.example.com.au+61 448 187 226Differentiators (for us to complete so doc must be editable)The format of the document needs to be easily modified when required. I have attached the company logos and branding colours / font etc. Thank youRegardsMiriam

Target Market(s)

Medium businesses Australian based

Industry/Entity Type

Travel Industry

Font styles to use
Sans Serif

Colors
abd036

Requirements
Must have
• Content Outlined and corporate colours. Must be easily editable.

```html
<!DOCTYPE html>
<html lang="en">
<head>
<meta charset="utf-8">
<title>Steadfast Voyage Partners – Capability Statement</title>
<link href="https://fonts.googleapis.com/css2?family=Montserrat:wght@400;500;600;700&display=swap" rel="stylesheet">
<style>
  :root{
    --green:#3fb44a;
    --lime:#abd036;
    --blue:#2f7fd0;
    --ink:#2f2f33;
    --grey:#55565a;
    --muted:#6a6b70;
    --paper:#fbfbfc;
    --stage:#e4e4e6;
  }
  *{box-sizing:border-box;margin:0;padding:0}
  html,body{width:1200px;height:1200px;overflow:hidden;background:var(--stage);font-family:"Montserrat",sans-serif;color:var(--ink)}
  .sheet{position:absolute;left:200px;top:39px;width:800px;height:1122px;background:var(--paper);overflow:hidden}
  .header{position:absolute;left:0;top:0;width:800px;height:141px;background:#f3f4f6}
  .brand-box{position:absolute;left:10px;top:11px;width:340px;height:130px;background:#fff;display:flex;flex-direction:column;justify-content:center;padding-left:26px}
  .brand-name{display:flex;align-items:center;gap:10px;font-size:25px;font-weight:600;color:var(--grey);line-height:1.05}
  .brand-name .mark{width:28px;height:28px;background:var(--lime);flex:none}
  .brand-tag{margin-top:12px;margin-left:38px;font-size:12px;font-weight:600;color:var(--lime);letter-spacing:.3px}
  .title{position:absolute;left:349px;top:56px;font-size:38px;font-weight:700;color:var(--green);letter-spacing:.3px}
  .stats{position:absolute;left:0;top:141px;width:800px;height:248px;background:linear-gradient(180deg,#e5e8eb 0%,#eef0f2 70%,#f7f8f9 100%)}
  .donut{position:absolute;top:37px;width:174px;height:174px}
  .donut.employee{left:40px}
  .donut.client{left:249px}
  .donut-label{position:absolute;inset:0;display:flex;flex-direction:column;align-items:center;justify-content:center;text-align:center;font-size:12px;line-height:1.2;color:var(--grey)}
  .donut-label b{font-size:24px;font-weight:700;margin-bottom:2px}
  .employee b{color:var(--blue)}
  .client b{color:var(--green)}
  .intro{position:absolute;left:456px;top:46px;width:312px;font-size:25px;line-height:36px;text-align:justify;text-align-last:left;color:var(--ink);font-weight:500}
  .main{position:absolute;left:34px;top:412px;width:474px}
  h1.competencies{font-size:34px;font-weight:700;color:var(--green);line-height:38px;white-space:nowrap}
  h1.competencies span{display:block;color:var(--grey);font-size:30px;line-height:38px}
  h2{font-size:24px;font-weight:700;color:var(--ink);line-height:31px}
  .main h2.snapshot{margin-top:14px}
  p{font-size:11px;line-height:14px;color:var(--muted);text-align:justify}
  .main p{margin-top:10px}
  .main h2.snapshot + p{margin-top:12px}
  .main h2.benefits{margin-top:20px;margin-bottom:16px}
  .main h2.affiliations{margin-top:24px}
  .side{position:absolute;left:522px;top:452px;width:248px}
  .side h2{margin-bottom:12px}
  .side p{margin-bottom:10px}
  .partners{position:absolute;left:34px;top:1008px;width:470px;display:flex;flex-direction:column;gap:30px}
  .partner-row{display:flex;gap:16px;align-items:center;height:22px}
  .partner{font-size:13px;font-weight:700;color:var(--grey);white-space:nowrap;display:flex;align-items:center;gap:5px}
  .partner i{display:inline-block;width:10px;height:10px;background:var(--blue)}
  .partner.red i{background:#d9232d}
  .partner.green i{background:var(--green);border-radius:50%}
  .awards{position:absolute;left:522px;top:676px;width:256px;height:320px}
  .badge{position:absolute;background:#fff}
  .badge.winner{left:32px;top:0;width:190px;height:136px}
  .badge.f18{left:0;top:141px;width:128px;height:178px}
  .badge.f17{left:128px;top:141px;width:128px;height:178px}
  .contact{position:absolute;left:522px;top:1003px;width:272px}
  .contact .name{font-size:19px;font-weight:700;color:var(--ink);margin-bottom:8px}
  .contact .row{display:flex;align-items:center;gap:8px;font-size:16px;color:var(--ink);margin-bottom:8px;white-space:nowrap}
  .contact .row.phone{font-weight:700}
  .contact .row.email{font-size:12.5px}
  .rule{position:absolute;left:116px;top:1091px;width:566px;height:2px;background:#a2a3a6}
  .web{position:absolute;left:0;width:800px;top:1100px;text-align:center;font-size:15px;color:var(--ink);display:flex;justify-content:center;align-items:center;gap:8px}
</style>
</head>
<body>
<main class="sheet">
  <header class="header">
    <div class="brand-box">
      <div class="brand-name"><span class="mark"></span>Steadfast Voyage<br>Partners</div>
      <div class="brand-tag">PEOPLE | SERVICE | TECHNOLOGY</div>
    </div>
    <div class="title">Capability Statement</div>
  </header>

  <section class="stats">
    <div class="donut employee">
      <svg width="174" height="174" viewBox="0 0 174 174">
        <defs>
          <linearGradient id="blueRing" x1="0" y1="0" x2="0" y2="1">
            <stop offset="0" stop-color="#2b6fc4"/><stop offset="1" stop-color="#3aa6e4"/>
          </linearGradient>
        </defs>
        <circle cx="87" cy="87" r="84" fill="#d9dcdf"/>
        <circle cx="87" cy="87" r="66" fill="none" stroke="#e4e6e8" stroke-width="26"/>
        <circle cx="87" cy="87" r="66" fill="none" stroke="url(#blueRing)" stroke-width="26" stroke-dasharray="352 415" transform="rotate(-90 87 87)"/>
        <circle cx="87" cy="87" r="53" fill="#fff"/>
      </svg>
      <div class="donut-label"><b>98%</b>of<br>Employee<br>retention</div>
    </div>
    <div class="donut client">
      <svg width="174" height="174" viewBox="0 0 174 174">
        <defs>
          <linearGradient id="greenRing" x1="0" y1="0" x2="0" y2="1">
            <stop offset="0" stop-color="#3fb44a"/><stop offset="1" stop-color="#abd036"/>
          </linearGradient>
        </defs>
        <circle cx="87" cy="87" r="84" fill="#d9dcdf"/>
        <circle cx="87" cy="87" r="66" fill="none" stroke="#e4e6e8" stroke-width="26"/>
        <circle cx="87" cy="87" r="66" fill="none" stroke="url(#greenRing)" stroke-width="26" stroke-dasharray="290 415" transform="rotate(-90 87 87)"/>
        <circle cx="87" cy="87" r="53" fill="#fff"/>
      </svg>
      <div class="donut-label"><b>96%</b>of<br>Client retention<br>result</div>
    </div>
    <div class="intro">Lorem Ipsum is simply dummy text of the printing and typesetting industry</div>
  </section>

  <section class="main">
    <h1 class="competencies">Our Core Competencies -<span>Service / People / Technology</span></h1>
    <h2 class="snapshot">A Company snapshot - Office location and website</h2>
    <p>Lorem Ipsum is simply dummy text of the printing and typesetting industry. Lorem Ipsum has been the industry's standard dummy text ever since the 1500s, when an unknown printer took a galley of type and scrambled it to make a type specimen book.</p>
    <p>Lorem Ipsum is simply dummy text of the printing and typesetting industry. Lorem Ipsum has been the industry's standard dummy text ever since the 1500s, when an unknown printer took a galley of type and scrambled it to make a type specimen book. It has survived not only five centuries, but also the leap into electronic typesetting, remaining essentially unchanged.</p>
    <h2 class="benefits">Performance / Key Benefits:</h2>
    <p>Lorem Ipsum is simply dummy text of the printing and typesetting industry. Lorem Ipsum has been the industry's standard dummy text ever since the 1500s, when an unknown printer took a galley of type and scrambled it to make a type specimen book. It has survived not only five centuries, but also the leap into electronic typesetting, remaining essentially unchanged. It was popularised in the 1960s with the release of Letraset sheets containing Lorem Ipsum passages, and more recently with desktop publishing software like Aldus PageMaker including versions of Lorem Ipsum.</p>
    <h2 class="affiliations">Affiliations &amp; Partnerships</h2>
  </section>

  <div class="partners">
    <div class="partner-row">
      <span class="partner"><i></i>Routewise</span>
      <span class="partner red"><i></i>Hollowfield</span>
      <span class="partner"><i></i>Skyrate</span>
      <span class="partner green"><i></i>Travel Guild</span>
      <span class="partner green"><i></i>Accredit</span>
    </div>
    <div class="partner-row">
      <span class="partner red"><i></i>Silverwing Club</span>
      <span class="partner"><i></i>FareCircle</span>
      <span class="partner green"><i></i>Journeysafe Tech</span>
    </div>
  </div>

  <aside class="side">
    <h2>Awards</h2>
    <p>Lorem Ipsum is simply dummy text of the printing and typesetting industry. Lorem Ipsum has been the industry's standard dummy text ever since the 1500s, when an unknown printer took a galley of type and scrambled it to make a type specimen book.</p>
    <p>Lorem Ipsum is simply dummy text of the printing and typesetting industry. Lorem Ipsum has been the industry's standard.</p>
  </aside>

  <div class="awards">
    <div class="badge winner"><svg width="190" height="136" role="img" aria-label="Industry award winner 2015 badge"><circle cx="95" cy="66" r="52" fill="#e6e7e9"/><circle cx="95" cy="32" r="18" fill="#abd036"/></svg></div>
    <div class="badge f18"><svg width="128" height="178" role="img" aria-label="Industry award finalist 2018 badge"><circle cx="64" cy="34" r="22" fill="#abd036"/><rect x="16" y="72" width="96" height="84" fill="#e6e7e9"/></svg></div>
    <div class="badge f17"><svg width="128" height="178" role="img" aria-label="Industry award finalist 2017 badge"><circle cx="64" cy="34" r="22" fill="#abd036"/><rect x="16" y="72" width="96" height="84" fill="#e6e7e9"/></svg></div>
  </div>

  <div class="contact">
    <div class="name">Marcus Van Heerden</div>
    <div class="row phone">
      <svg width="14" height="14" viewBox="0 0 24 24"><path d="M6.6 10.8a15.1 15.1 0 006.6 6.6l2.2-2.2a1 1 0 011-.25 11.4 11.4 0 003.6.57 1 1 0 011 1V20a1 1 0 01-1 1A17 17 0 013 4a1 1 0 011-1h3.5a1 1 0 011 1c0 1.25.2 2.45.57 3.57a1 1 0 01-.25 1z" fill="#2f2f33"/></svg>
      +61 455 903 618
    </div>
    <div class="row email">
      <svg width="14" height="12" viewBox="0 0 14 12"><rect x="0.5" y="0.5" width="13" height="11" fill="#2f2f33"/><path d="M1 1l6 5 6-5" stroke="#fff" stroke-width="1.3" fill="none"/></svg>
      marcus@svpartners.example.com.au
    </div>
  </div>

  <div class="rule"></div>
  <div class="web">
    <svg width="9" height="9" viewBox="0 0 10 10"><circle cx="5" cy="5" r="4.5" fill="#55565a"/></svg>
    www.steadfastvoyagepartners.example.com.au
  </div>
</main>
</body>
</html>
```